Flyer Tally Your Ledger Free

Hi
Can you please design me a DL Flyer for: Tally Your Ledger Free
Info:
Starting a new Business ?
Want to save on bookkeeping fees for your existing business?

You can now save 1000's off bookkeeping fees by Doing it Yourself.

Using our Bookkeeper software you simply key in the information as you go.

We offer one on one training, backup and support.
We can assist you with BAS Preparation and Payrol Advice.

Add Modules as required:
Point of Sale Module
Jobs Management Module
Website Intergration Module

Fee set up assistance and training.

Lets get the ball rolling: 1300 642 815
www.tylfr.com.au
admin@tylfr.com.au (use the logo thing you made)

Target Market(s)

Small Business

Colors
ec1f27
f04a50
f59296
fcdcdc
ffffff

Requirements
Nice to have
• image/s related to bookkeeping

```html
<!DOCTYPE html>
<html lang="en">
<head>
<meta charset="utf-8">
<title>Tally Your Ledger Free – DL Flyer</title>
<link href="https://fonts.googleapis.com/css2?family=Montserrat:wght@400;500;600;700;800;900&display=swap" rel="stylesheet">
<style>
  :root{
    --red:#ec1f27;
    --red-soft:#f04a50;
    --pink:#f59296;
    --blush:#fcdcdc;
    --white:#ffffff;
    --ink:#1d1d1f;
    --charcoal:#3a3a3d;
    --grey:#6d6e72;
    --stage:#e8e5e0;
  }
  *{box-sizing:border-box;margin:0;padding:0}
  html,body{width:1200px;height:842px;overflow:hidden}
  body{background:var(--stage);font-family:"Montserrat",sans-serif;position:relative}
  .flyer{position:absolute;top:29px;width:370px;height:784px;background:var(--white);overflow:hidden;box-shadow:0 6px 18px rgba(0,0,0,.12)}
  .flyer--front{left:205px}
  .flyer--back{left:625px}
  .layer{position:absolute;left:0;width:100%}

  /* front */
  .brand{position:absolute;top:34px;left:28px;display:flex;align-items:center;gap:12px}
  .brand__dot{width:34px;height:34px;border-radius:50%;background:var(--red)}
  .brand__name{font-weight:700;font-size:21px;color:var(--red);letter-spacing:-.2px}
  .front-header{top:100px;height:170px;background:var(--red);clip-path:polygon(0 0,100% 0,100% 76%,60% 76%,53% 100%,0 100%)}
  .front-photo{top:205px;height:400px;background:linear-gradient(160deg,#c9c2dc 0%,#a79fbf 35%,#6f6b7a 60%,#d8d2c4 85%,#9a93a8 100%)}
  .headline{position:absolute;top:118px;left:28px;color:var(--white);line-height:1}
  .headline__top{font-size:27px;font-weight:600;letter-spacing:.5px}
  .headline__main{font-size:31px;font-weight:900;margin-top:2px}
  .headline__rule{width:190px;height:1px;background:rgba(255,255,255,.8);margin:10px 0 8px}
  .headline__sub{font-size:13.5px;font-weight:500;line-height:1.3}
  .offer-block{top:470px;height:200px;background:var(--red);clip-path:polygon(0 28%,50% 28%,58% 0,100% 0,100% 100%,0 100%)}
  .offer{position:absolute;top:540px;left:28px;color:var(--white);line-height:1.08}
  .offer__lead{font-size:20px;font-weight:700}
  .offer__big{font-size:40px;font-weight:900;letter-spacing:.5px}
  .offer__rest{font-size:21px;font-weight:800}
  .cta-band{top:670px;height:40px;background:var(--charcoal);color:var(--white);font-size:16px;font-weight:700;letter-spacing:.6px;display:flex;align-items:center;padding-left:28px}
  .contact{position:absolute;left:28px}
  .contact--phone{top:718px;display:flex;align-items:center;gap:8px;color:var(--red);font-size:25px;font-weight:800}
  .contact--lines{top:756px;font-size:11.5px;color:var(--ink);font-weight:500;display:flex;gap:8px;align-items:center}
  .contact--lines .sep{color:var(--red)}
  .icon{flex:none}

  /* back */
  .back-photo{top:150px;height:330px;background:linear-gradient(120deg,#e6e3df 0%,#d9d4cd 40%,#b89a7a 70%,#8b8e90 100%)}
  .back-header{top:0;height:370px;background:var(--red);clip-path:polygon(0 0,100% 0,100% 72%,0 100%)}
  .intro{position:absolute;top:44px;left:28px;width:300px;color:var(--white)}
  .intro__text{font-size:13.5px;line-height:1.35;font-weight:500}
  .intro__text strong{font-weight:800}
  .intro__rule{width:250px;height:1px;background:rgba(255,255,255,.85);margin:14px 0 12px}
  .intro__offer{font-size:22px;font-weight:800;line-height:1.2}
  .back-panel{top:430px;height:354px;background:var(--white);clip-path:polygon(0 18%,100% 0,100% 100%,0 100%)}
  .assist{position:absolute;top:505px;left:28px;color:var(--red);font-size:20px;font-weight:800;line-height:1.2}
  .modules{position:absolute;top:592px;left:28px;right:20px;display:flex}
  .module{flex:1;padding:0 8px;border-left:1px solid var(--pink)}
  .module:first-child{border-left:none;padding-left:0}
  .module__label{margin-top:8px;font-size:12px;line-height:1.25;color:var(--ink);font-weight:500}
  .fee-band{top:690px;height:32px;background:var(--red);color:var(--white);font-size:12.5px;font-weight:800;letter-spacing:.4px;display:flex;align-items:center;padding-left:28px}
  .back-phone{position:absolute;top:730px;left:28px;display:flex;align-items:center;gap:8px;font-size:25px;font-weight:800;color:var(--ink)}
  .back-web{position:absolute;top:762px;left:28px;display:flex;align-items:center;gap:6px;font-size:12.5px;font-weight:600;color:var(--ink)}
</style>
</head>
<body>

<section class="flyer flyer--front">
  <div class="brand">
    <span class="brand__dot"></span>
    <span class="brand__name">Tally Your Ledger Free</span>
  </div>
  <div class="layer front-photo" role="img" aria-label="Photo of stacked office binders labelled Salaries and Payroll"></div>
  <div class="layer front-header"></div>
  <div class="headline">
    <div class="headline__top">STARTING A</div>
    <div class="headline__main">NEW BUSINESS?</div>
    <div class="headline__rule"></div>
    <div class="headline__sub">Want to save on bookkeeping fees<br>for your existing business?</div>
  </div>
  <div class="layer offer-block"></div>
  <div class="offer">
    <div class="offer__lead">You can now Save</div>
    <div class="offer__big">1000's OFF</div>
    <div class="offer__rest">bookkeeping fees by<br>Doing it Yourself.</div>
  </div>
  <div class="layer cta-band">LETS GET THE BALL ROLLING:</div>
  <div class="contact contact--phone">
    <svg class="icon" width="24" height="24" viewBox="0 0 24 24"><circle cx="12" cy="12" r="10.5" fill="none" stroke="var(--red)" stroke-width="2"/><path d="M9 7.5c.6 3.6 3.3 7 7 8.5l1-1.8-2-1.2-1 1c-1.6-.8-2.8-2.1-3.5-3.6l1-1-1-2.1z" fill="var(--red)"/></svg>
    1300 642 815
  </div>
  <div class="contact contact--lines">
    <span>✉ admin@tylfr.com.au</span><span class="sep">|</span><span>⊕ www.tylfr.com.au</span>
  </div>
</section>

<section class="flyer flyer--back">
  <div class="layer back-photo" role="img" aria-label="Photo of a smiling woman at a desk reviewing papers beside a laptop"></div>
  <div class="layer back-header"></div>
  <div class="intro">
    <p class="intro__text">Using our <strong>Bookkeeper Software</strong><br>you simply key in the information<br>as you go.</p>
    <div class="intro__rule"></div>
    <p class="intro__offer">We offer<br>One on one Training,<br>Backup and Support.</p>
  </div>
  <div class="layer back-panel"></div>
  <p class="assist">We can assist you<br>with BAS Preparation and<br>Payrol Advice.</p>
  <div class="modules">
    <div class="module">
      <svg width="30" height="26" viewBox="0 0 30 26"><rect x="2" y="2" width="18" height="12" rx="1" fill="none" stroke="var(--red)" stroke-width="1.6"/><rect x="4" y="17" width="24" height="7" rx="1" fill="none" stroke="var(--red)" stroke-width="1.6"/><path d="M22 8h6v9" fill="none" stroke="var(--red)" stroke-width="1.6"/></svg>
      <p class="module__label">Point of<br>Sale<br>Module</p>
    </div>
    <div class="module">
      <svg width="30" height="26" viewBox="0 0 30 26"><rect x="3" y="2" width="16" height="22" rx="1" fill="none" stroke="var(--red)" stroke-width="1.6"/><path d="M6 8h10M6 12h10M6 16h6" stroke="var(--red)" stroke-width="1.6"/><circle cx="23" cy="17" r="4.5" fill="none" stroke="var(--red)" stroke-width="1.6"/></svg>
      <p class="module__label">Jobs<br>Management<br>Module</p>
    </div>
    <div class="module">
      <svg width="30" height="26" viewBox="0 0 30 26"><rect x="2" y="2" width="26" height="18" rx="1" fill="none" stroke="var(--red)" stroke-width="1.6"/><path d="M2 7h26M6 11h8M6 15h12M18 11h6" stroke="var(--red)" stroke-width="1.6"/></svg>
      <p class="module__label">Website<br>Intergration<br>Module</p>
    </div>
  </div>
  <div class="layer fee-band">FEE SET UP ASSISTANCE AND TRAINING</div>
  <div class="back-phone">
    <svg class="icon" width="24" height="24" viewBox="0 0 24 24"><circle cx="12" cy="12" r="10.5" fill="none" stroke="var(--red)" stroke-width="2"/><path d="M9 7.5c.6 3.6 3.3 7 7 8.5l1-1.8-2-1.2-1 1c-1.6-.8-2.8-2.1-3.5-3.6l1-1-1-2.1z" fill="var(--red)"/></svg>
    1300 642 815
  </div>
  <div class="back-web"><span style="color:var(--red)">⊕</span> www.tylfr.com.au</div>
</section>

</body>
</html>
```